Wordpress theme for new e-commerce tropical furniture manufacturing business

We want to develop a Wordpress theme to suit our new Reefline Furniture website currently under development, business details as below.
Please see attached logo design for ideas of the design. This logo will be used as - letterhead, business cards, furniture labels etc.
We are a small Australian family business that provides products as below:
- Hand Crafted, Creative Tropical design Furniture,
(manufacture and sales).
- Specializing in mirror- wall art
- One off – designs 'made to order'.
- Individually badged pieces, each with an identification production number.
Materials used that may be incorporated in the 'web theme designs' are: Bamboo, Wood, Waves, Ocean, Shells, Tropical flowers (eg; Hibiscus, Frangipani, Heliconias, Stralitzias), Palms,Pandanus & Stone etc. etc.
Industry/Entity Type
E-Commerce
Colors
Designer to choose colors to be used in the design.
Look and feel
Each slider illustrates characteristics of the customer's brand and the style your logo design should communicate.

```html
<!DOCTYPE html>
<html lang="en">
<head>
<meta charset="utf-8">
<title>Reefline Furniture</title>
<link href="https://fonts.googleapis.com/css2?family=Hind:wght@400;500;600&display=swap" rel="stylesheet">
<style>
:root{
  --sky-top:#4a9fd6;
  --sky-mid:#bfe0f2;
  --sea:#5fb6c9;
  --sand:#e9dcc6;
  --nav:#4aa3dd;
  --nav-dark:#2f8fce;
  --nav-line:#7cc0ea;
  --blue-head:#1a8fd6;
  --green-head:#6ea52c;
  --orange-head:#f2a71b;
  --btn:#f6ac22;
  --btn-dark:#e58f0c;
  --text:#444;
  --muted:#8a8a8a;
  --rule:#e3e3e3;
  --footer:#2a1b10;
  --footer-bar:#3a2717;
  --footer-text:#f3eee8;
  --white:#fff;
  --wood-dark:#6b3d1c;
  --wood:#b5753d;
  --wood-light:#d9b07a;
  --teal:#2a8aa0;
}
*{margin:0;padding:0;box-sizing:border-box}
html,body{width:786px;height:1200px;overflow:hidden}
body{
  position:relative;
  font-family:"Hind",Arial,sans-serif;
  color:var(--text);
  background:linear-gradient(to bottom,var(--sky-top) 0,var(--sky-mid) 90px,var(--sea) 104px,var(--sea) 180px,var(--sand) 330px,var(--sand) 1200px);
}
.abs{position:absolute}
.brand{left:0;width:786px;top:38px;text-align:center}
.brand-name{font-size:27px;font-weight:600;color:#1f8fd0;letter-spacing:1px;line-height:1}
.brand-url{font-size:7px;color:#4a6a7e;letter-spacing:1.4px;margin-top:7px}
.nav{left:97px;top:103px;width:595px;height:33px;background:linear-gradient(var(--nav),var(--nav-dark));display:flex}
.nav a{color:var(--white);text-decoration:none;font-size:11px;font-weight:500;line-height:35px;text-align:center;border-right:1px solid var(--nav-line)}
.nav a:last-child{border-right:none}
.slider{left:97px;top:136px;width:595px;height:232px;
  background:linear-gradient(to bottom,#e7e2d6 0,#2f8ea5 14%,#23778e 40%,#c9a464 62%,#d8b985 80%,#e6d3ad 100%)}
.slide-arrow{top:230px;width:24px;height:38px;background:rgba(40,40,40,.45)}
.content{left:97px;top:368px;width:595px;height:638px;background:var(--white)}
.h-blue{color:var(--blue-head);font-size:14px;font-weight:500}
.h-green{color:var(--green-head);font-size:14px;font-weight:500}
.h-orange{color:var(--orange-head);font-size:14px;font-weight:500}
.h-dark{color:#4a3a2a;font-size:13px;font-weight:500}
.feat-img{top:418px;width:180px;height:69px}
.feat-title{font-size:13px;color:#333;top:492px;font-weight:400}
.feat-desc{font-size:8.3px;color:var(--muted);line-height:12.5px;top:509px;width:182px}
.dash{left:113px;top:552px;width:372px;border-top:1px dashed #e0b870}
.prod-img{left:113px;width:165px;height:99px;border:1px solid #ddd;background:#fff;padding:12px 30px}
.prod-img .fill{width:100%;height:100%;border-radius:3px}
.prod-title{left:289px;font-size:13px;color:var(--orange-head);font-weight:400}
.prod-body{left:289px;width:198px;font-size:8.3px;line-height:13.8px;color:var(--muted)}
.btn{left:289px;width:72px;height:20px;border-radius:2px;background:linear-gradient(var(--btn),var(--btn-dark));color:var(--white);font-size:7.5px;font-weight:600;text-align:center;line-height:21px}
.divider{left:502px;top:392px;height:598px;border-left:1px solid var(--rule)}
.side-list{left:520px;list-style:none}
.side-list li{font-size:8.3px;color:#777;height:18.4px;padding-left:12px;position:relative;line-height:12px}
.side-list li::before{content:"";position:absolute;left:2px;top:3px;border-left:3px solid #999;border-top:3px solid transparent;border-bottom:3px solid transparent}
.blog-thumb{left:520px;width:55px;height:41px}
.blog-title{left:581px;font-size:8.5px;color:#222;font-weight:500}
.blog-text{left:581px;width:100px;font-size:6.6px;line-height:9.5px;color:var(--muted)}
.footer{left:97px;top:1006px;width:595px;height:176px;background:var(--footer)}
.footer-bar{left:97px;top:1150px;width:595px;height:32px;background:var(--footer-bar)}
.copy{left:119px;top:1164px;font-size:6.6px;color:#b7a796}
.f-col{top:1031px}
.f-col h4{font-size:10px;font-weight:600;color:var(--white);margin-bottom:3px}
.f-col p{font-size:8px;color:var(--footer-text);line-height:15px}
.social{left:490px;top:1099px;display:flex;gap:6px}
.social span{width:16px;height:16px;border-radius:50%;background:var(--white)}
</style>
</head>
<body>
  <header class="abs brand">
    <div class="brand-name">Reefline Furniture</div>
    <div class="brand-url">www.reeflinefurniture.com.au</div>
  </header>

  <nav class="abs nav">
    <a style="width:73px">HOME</a>
    <a style="width:83px">ABOUT US</a>
    <a style="width:88px">PRODUCTS</a>
    <a style="width:88px">BLOG POST</a>
    <a style="width:81px">WALL ART</a>
    <a style="width:79px">SUPPORT</a>
    <a style="width:103px">CONTACT US</a>
  </nav>

  <div class="abs slider" role="img" aria-label="Lounge interior with wicker armchairs, teal sofa and brass table lamps"></div>
  <div class="abs slide-arrow" style="left:97px"><svg width="24" height="38"><path d="M14 11 L8 19 L14 27" stroke="#fff" stroke-width="1.5" fill="none"/></svg></div>
  <div class="abs slide-arrow" style="left:668px"><svg width="24" height="38"><path d="M10 11 L16 19 L10 27" stroke="#fff" stroke-width="1.5" fill="none"/></svg></div>

  <main class="abs content"></main>

  <h2 class="abs h-blue" style="left:110px;top:394px">Featured Products</h2>
  <div class="abs feat-img" style="left:110px;background:linear-gradient(to bottom,#5a2f16 0,#a5612c 45%,#c88446 70%,#8a4a22 100%)" role="img" aria-label="Wooden writing desk with drawers"></div>
  <div class="abs feat-img" style="left:309px;background:linear-gradient(to bottom,#c8a878 0,#d9b886 40%,#b08655 75%,#8f6a42 100%)" role="img" aria-label="Timber Adirondack chairs set"></div>
  <h3 class="abs feat-title" style="left:111px">Donec convallis pede</h3>
  <h3 class="abs feat-title" style="left:309px">Malesuada nec ultricies sit</h3>
  <p class="abs feat-desc" style="left:111px">Malesuada nec ultricies sit amet porttitor mattis enim In massa libero interdum nec</p>
  <p class="abs feat-desc" style="left:309px">Malesuada nec ultricies sit amet porttitor mattis enim In massa libero interdum nec</p>
  <div class="abs dash"></div>

  <h2 class="abs h-green" style="left:113px;top:572px">Our More Products</h2>

  <div class="abs prod-img" style="top:600px"><div class="fill" role="img" aria-label="Wooden A-frame chicken coop" style="background:linear-gradient(to bottom,#c98a55,#a55e30 60%,#7c5a3a)"></div></div>
  <h3 class="abs prod-title" style="top:598px">Donec convallis pede venenatis</h3>
  <p class="abs prod-body" style="top:617px">Vivamus porttitor purus nisi eleifend libero a tempus libero lectus feugiat felis Morbi diam mauris viverra in gravida eu mattis in ante Morbi eget arcu Morbi porta libero id ullamcorper nonummy nibh ligula</p>
  <div class="abs btn" style="top:676px">READ MORE</div>

  <div class="abs prod-img" style="top:724px;padding:0;background:linear-gradient(to bottom,#d9d7d3,#c9c6c1)"><div class="fill" role="img" aria-label="Two wooden barrel stools" style="border-radius:0;background:linear-gradient(to bottom,rgba(150,115,80,.15),rgba(140,100,65,.45))"></div></div>
  <h3 class="abs prod-title" style="top:722px">Etiam est nunc venenatis</h3>
  <p class="abs prod-body" style="top:741px">Vivamus porttitor purus nisi eleifend libero a tempus libero lectus feugiat felis Morbi diam mauris viverra in gravida eu mattis in ante Morbi eget arcu Morbi porta libero id ullamcorper nonummy nibh ligula</p>
  <div class="abs btn" style="top:800px">READ MORE</div>

  <div class="abs prod-img" style="top:848px"><div class="fill" role="img" aria-label="Stack of woven rattan baskets" style="background:linear-gradient(to bottom,#c99a78,#b57e58 60%,#e6d8cc)"></div></div>
  <h3 class="abs prod-title" style="top:846px">Nunc porta convallis pede</h3>
  <p class="abs prod-body" style="top:865px">Vivamus porttitor purus nisi eleifend libero a tempus libero lectus feugiat felis Morbi diam mauris viverra in gravida eu mattis in ante Morbi eget arcu Morbi porta libero id ullamcorper nonummy nibh ligula</p>
  <div class="abs btn" style="top:924px">READ MORE</div>

  <div class="abs divider"></div>

  <h2 class="abs h-orange" style="left:520px;top:397px">Our Categories</h2>
  <ul class="abs side-list" style="top:422px">
    <li>Etiam est nunc venenatis</li><li>Tristique imperdiet</li><li>Cum sociis</li><li>Natoque penatibus</li><li>Magnis dis parturient</li><li>Montes nascetur</li><li>Ridiculus mus</li><li>Facilisis massa Etiam</li><li>Sed porta Suspendisse</li><li>Quam leo molestie</li>
  </ul>

  <h2 class="abs h-dark" style="left:520px;top:624px">Latest Blog Post</h2>
  <div class="abs blog-thumb" style="top:648px;background:linear-gradient(to bottom,#4a2c14,#9a6434 60%,#5a3a1e)" role="img" aria-label="Carved wooden bowl"></div>
  <div class="abs blog-title" style="top:648px">Donec scelerisque</div>
  <p class="abs blog-text" style="top:660px">Ut ante enim dapibus male-suada fringilla eu condimentum quis tellus Aene</p>
  <div class="abs blog-thumb" style="top:701px;background:linear-gradient(to bottom,#d8cdbd,#b88650 55%,#7a4c24)" role="img" aria-label="Wooden cabinet"></div>
  <div class="abs blog-title" style="top:701px">Class aptent taciti</div>
  <p class="abs blog-text" style="top:713px">Ut ante enim dapibus male-suada fringilla eu condimentum quis tellus Aene</p>
  <div class="abs blog-thumb" style="top:754px;background:linear-gradient(to bottom,#6a3a18,#a8692f 55%,#6e401c)" role="img" aria-label="Timber entertainment unit"></div>
  <div class="abs blog-title" style="top:754px">Morbi porta libero</div>
  <p class="abs blog-text" style="top:766px">Ut ante enim dapibus male-suada fringilla eu condimentum quis tellus Aene</p>

  <h2 class="abs h-dark" style="left:520px;top:817px">Resources &amp; Links</h2>
  <ul class="abs side-list" style="top:841px">
    <li>Natoque penatibus</li><li>Magnis dis parturient</li><li>Montes nascetur</li><li>Ridiculus mus</li><li>Facilisis massa Etiam</li><li>Sed porta Suspendisse</li><li>Quam leo molestie</li>
  </ul>

  <footer class="abs footer"></footer>
  <div class="abs f-col" style="left:123px"><h4>QUICK LINKS</h4><p>Etiam est nunc</p><p>Benenatis tristique</p><p>Eu imperdiet ac nisl</p><p>Cum sociis</p><p>Natoque</p></div>
  <div class="abs f-col" style="left:235px"><h4>LATEST POSTS</h4><p>Etiam est nunc</p><p>Benenatis tristique</p><p>Eu imperdiet ac nisl</p><p>Cum sociis</p><p>Natoque</p></div>
  <div class="abs f-col" style="left:357px"><h4>FEATURED POSTS</h4><p>Etiam est nunc</p><p>Benenatis tristique</p><p>Eu imperdiet ac nisl</p><p>Cum sociis</p><p>Natoque</p></div>
  <div class="abs f-col" style="left:492px"><h4>SUPPORT</h4><p>Etiam est nunc</p><p>Benenatis tristique</p><p>Eu imperdiet ac ni</p></div>
  <div class="abs social"><span></span><span></span><span></span></div>
  <div class="abs footer-bar"></div>
  <p class="abs copy">© 2014 Company Name &nbsp;All right reserved &nbsp;Term of Use</p>
</body>
</html>
```